Lantern Crest Gathering Day 2021

I am looking to create a flyer for a one day prayer retreat our church is organizing. This flyer will be posted on social media, websites, mobile apps, and will also be printed so it can be mailed to people.

I am looking for something professional, with good use of our logo and band colors (logo colors).

I am counting on the designer's skill, creativity, art and knowledge of media communication to produce a flyer that will effectively and quickly convey the message we are trying to spread.

CONTENT OF THE FLYER:
Event title: Lantern Crest Gathering Day
Date: Tuesday July 2nd, 2021
Time: 11:00AM - 7:00PM
Brindlewick Hotel, 4817 Fennimore Street, Portland, Maine 04102 (Room: Thistlemoor)
Event Key words to highlight what the event is about: Prayer, Fasting, Worship, Prophecy, Revival.
Key phrases:
A one day prayer retreat.
Jesus Chris is Lord

Contact info:
www.velunto.org
Phone: 207 555 0143
Email: contact@quillbrookfold.org

```html
<!DOCTYPE html>
<html lang="en">
<head>
<meta charset="utf-8">
<title>Lantern Crest Gathering Day 2021</title>
<link rel="stylesheet" href="https://fonts.googleapis.com/css2?family=Pacifico&family=Mulish:wght@600;700;800&display=swap">
<style>
  :root {
    --page-bg: #ececec;
    --navy: #0f3a63;
    --navy-deep: #0a2641;
    --maroon: #6f2d30;
    --maroon-shadow: #3a2a2c;
    --white: #ffffff;
    --gold: #ffe21a;
    --blush: #f7ddd4;
    --blush-text: #f6d5cc;
    --flame: #f5a11c;
    --photo-light: #e9eaec;
    --photo-mid: #b9a8a2;
    --photo-warm: #b5473c;
  }
  * { box-sizing: border-box; margin: 0; padding: 0; }
  html, body {
    width: 1200px; height: 840px; overflow: hidden;
    background: var(--page-bg);
  }
  .flyer {
    position: absolute; left: 290px; top: 20px;
    width: 620px; height: 800px; overflow: hidden;
    box-shadow: 0 10px 30px rgba(0,0,0,.25);
    font-family: "Mulish", sans-serif;
  }
  .flyer__photo {
    position: absolute; inset: 0;
    background:
      radial-gradient(ellipse 260px 300px at 62% 50%, #e8b9a0 0%, rgba(232,185,160,.7) 45%, rgba(232,185,160,0) 100%),
      linear-gradient(125deg, var(--photo-light) 0%, var(--photo-light) 25%, var(--photo-mid) 50%, var(--photo-warm) 85%);
  }
  .flyer__title {
    position: absolute; left: 58px; top: 40px;
    font-family: "Pacifico", cursive;
    font-size: 50px; line-height: 76px;
    color: var(--navy);
  }
  .flyer__bands { position: absolute; inset: 0; }
  .brand-box {
    position: absolute; left: 420px; top: 560px;
    width: 172px; height: 160px;
    background: var(--navy);
    display: flex; flex-direction: column; align-items: center; justify-content: center;
    gap: 10px;
    border-bottom: 20px solid var(--navy-deep);
  }
  .brand-box__dot { width: 16px; height: 16px; border-radius: 50%; background: var(--flame); }
  .brand-box__name { color: var(--white); font-weight: 700; font-size: 28px; letter-spacing: 1px; }
  .details {
    position: absolute; left: 20px; top: 594px; width: 390px;
    text-align: center;
  }
  .details__lead { color: var(--white); font-weight: 800; font-size: 22px; line-height: 27px; }
  .details__when {
    color: var(--gold); font-weight: 700; font-size: 14.5px; line-height: 18px; margin-top: 8px;
  }
  .keywords {
    position: absolute; left: 0; right: 0; top: 732px;
    color: var(--blush-text); font-weight: 700; font-size: 19px; letter-spacing: .5px;
    text-align: center; white-space: nowrap;
  }
  .contact-strip {
    position: absolute; left: 0; right: 0; bottom: 0; height: 30px;
    background: var(--blush);
    color: var(--maroon); font-weight: 700; font-size: 12.5px;
    display: flex; align-items: center; justify-content: center; gap: 10px;
  }
</style>
</head>
<body>
  <main class="flyer">
    <div class="flyer__photo" role="img" aria-label="Photograph of clasped hands in prayer, a person in a red knit sweater"></div>

    <h1 class="flyer__title">Lantern<br>Crest<br>Gathering<br>Day</h1>

    <svg class="flyer__bands" width="620" height="800" viewBox="0 0 620 800" aria-hidden="true">
      <polygon points="0,446 420,590 420,602 0,460" fill="var(--maroon-shadow)"/>
      <polygon points="0,458 410,600 620,600 620,800 0,800" fill="var(--maroon)"/>
    </svg>

    <div class="brand-box">
      <span class="brand-box__dot"></span>
      <span class="brand-box__name">VELUNTO</span>
    </div>

    <section class="details">
      <p class="details__lead">A one day prayer retreat.<br>Jesus Chris is Lord</p>
      <p class="details__when">Tuesday July 2nd, 2021 | 11:00AM - 7:00PM<br>Brindlewick Hotel, 4817 Fennimore Street, Portland,<br>Maine 04102 (Room: Thistlemoor)</p>
    </section>

    <p class="keywords">Prayer, | Fasting, | Worship | Prophecy | Revival.</p>

    <footer class="contact-strip">
      <span>www.velunto.org</span><span>|</span>
      <span>Phone: 207 555 0143</span><span>|</span>
      <span>Email: contact@quillbrookfold.org</span>
    </footer>
  </main>
</body>
</html>
```